Corporate speaking flyer for email

Redesign existing and very lame flyer. This is for my speaking business to be used as an introduction of content and style and my presentations. More photos can be provided. As you will see I'm an adventurer who makes part of my living from speaking about my adventures. The bio describes the general gist of that. There is more I could say but wanting to keep it pretty brief so as not to bore potential clients. Having said that I'd like to try and capture them in the first instance.

Target Market(s)

Corporate, clubs, events

Industry/Entity Type

Business

Requirements
Must have
• bio and references. Content provided. Feel free to edit.
Nice to have
• Surprise me!
Should not have
• Rude words.

```html
<!DOCTYPE html>
<html lang="en">
<head>
<meta charset="utf-8">
<title>Sam Corwell – Speaker Flyer</title>
<link href="https://fonts.googleapis.com/css2?family=EB+Garamond:ital,wght@0,400;0,500;0,700;1,400&display=swap" rel="stylesheet">
<style>
  :root {
    --indigo: #2d2a86;
    --indigo-deep: #221f6e;
    --indigo-light: #3d39a6;
    --silver: #c9c9cf;
    --paper: #ffffff;
    --ink: #1c1a3a;
    --backdrop: #e9e7ee;
  }
  * { box-sizing: border-box; margin: 0; padding: 0; }
  html, body { width: 966px; height: 1200px; overflow: hidden; background: var(--backdrop); }
  body { font-family: "EB Garamond", Georgia, serif; color: var(--ink); position: relative; }

  .page {
    position: absolute; width: 460px; height: 575px;
    background: var(--paper); overflow: hidden;
    box-shadow: 0 3px 10px rgba(0,0,0,.18);
  }
  .page--cover { left: 16px; top: 16px; }
  .page--about { left: 490px; top: 16px; }
  .page--praise { left: 16px; top: 605px; }
  .page--closing { left: 490px; top: 605px; }

  .page-art { position: absolute; inset: 0; width: 460px; height: 575px; }

  /* cover */
  .speaker-name {
    position: absolute; top: 152px; left: 0; width: 100%; text-align: center;
    font-weight: 700; font-size: 38px; color: var(--indigo-deep); letter-spacing: .5px;
  }
  .tagline {
    position: absolute; top: 205px; left: 0; width: 100%; text-align: center;
    font-weight: 500; font-size: 20px; letter-spacing: 4px; color: var(--indigo-deep);
  }
  .contact-list { position: absolute; left: 46px; top: 495px; list-style: none; }
  .contact-list li {
    display: flex; align-items: center; gap: 6px; height: 22px;
    color: #fff; font-size: 6.5px; font-weight: 500;
  }
  .contact-list svg { width: 13px; height: 13px; }

  /* about */
  .section-title { position: absolute; color: #fff; font-size: 17px; font-weight: 400; }
  .about-title { top: 12px; left: 25px; }
  .bio { position: absolute; left: 19px; top: 42px; width: 422px; color: #fff; }
  .bio p { font-size: 7.1px; line-height: 1.36; margin-bottom: 7.5px; }
  .clients-title { position: absolute; top: 362px; left: 20px; font-size: 16px; font-weight: 500; color: var(--indigo-deep); }

  /* testimonials */
  .quote-row { position: absolute; left: 18px; right: 20px; display: flex; gap: 12px; align-items: flex-start; }
  .client-tag {
    flex: 0 0 137px; min-height: 20px; background: var(--indigo);
    color: #fff; font-size: 6.6px; line-height: 1.2; text-align: center;
    display: flex; align-items: center; justify-content: center; padding: 3px 5px;
    letter-spacing: .2px;
  }
  .client-quote { flex: 1; font-size: 6.6px; line-height: 1.3; text-align: justify; color: #222; }
  .client-quote--spaced { letter-spacing: .45px; line-height: 1.32; }

  /* closing */
  .closing-quote {
    position: absolute; left: 215px; top: 418px; width: 220px; text-align: right;
    color: #fff; font-size: 10px; letter-spacing: 1px; line-height: 1.3;
  }
  .closing-quote small { display: block; font-size: 5.8px; margin-top: 8px; letter-spacing: .8px; }
  .site-link { position: absolute; right: 22px; bottom: 12px; color: #fff; font-size: 6.5px; letter-spacing: 1px; }
</style>
</head>
<body>

<!-- Page 1: cover -->
<section class="page page--cover">
  <svg class="page-art" viewBox="0 0 460 575" aria-hidden="true">
    <defs>
      <linearGradient id="indigoFill" x1="0" y1="0" x2="1" y2="1">
        <stop offset="0" stop-color="#2a2780"/><stop offset="1" stop-color="#3936a0"/>
      </linearGradient>
      <linearGradient id="silverFill" x1="0" y1="0" x2="1" y2="0">
        <stop offset="0" stop-color="#e4e4e8"/><stop offset=".5" stop-color="#b9b9c1"/><stop offset="1" stop-color="#e4e4e8"/>
      </linearGradient>
      <linearGradient id="stageFill" x1="0" y1="0" x2="0" y2="1">
        <stop offset="0" stop-color="#9a9a9a"/><stop offset=".55" stop-color="#5e5e5e"/><stop offset="1" stop-color="#2e2e2e"/>
      </linearGradient>
    </defs>
    <path d="M0 0H460V100C340 150 190 152 0 112Z" fill="url(#indigoFill)"/>
    <path d="M0 112C190 152 340 150 460 100V112C340 164 190 166 0 126Z" fill="url(#silverFill)"/>
    <rect x="0" y="250" width="460" height="255" fill="url(#stageFill)" role="img" aria-label="Black and white photo of the speaker presenting on stage to a seated audience"/>
    <path d="M0 500C130 470 300 462 460 485V492C300 472 130 478 0 510Z" fill="url(#silverFill)"/>
    <path d="M0 510C130 478 300 472 460 492V575H0Z" fill="url(#indigoFill)"/>
  </svg>
  <h1 class="speaker-name">Sam Corwell</h1>
  <p class="tagline">“Anything is Possible”</p>
  <ul class="contact-list">
    <li>
      <svg viewBox="0 0 16 16" fill="#fff"><path d="M4 1l2.5 3-1.5 2c1 2 3 4 5 5l2-1.5 3 2.5-1.5 2.5C8 15 1 8 1.5 2.5Z"/></svg>
      : +64 (0)21 000 1234 / +64 (0)7 000 5678
    </li>
    <li>
      <svg viewBox="0 0 16 16" fill="none" stroke="#fff" stroke-width="1.6"><rect x="1.5" y="3.5" width="13" height="9"/><path d="M1.5 3.5L8 9l6.5-5.5"/></svg>
      : sam@corwell.co.nz
    </li>
    <li>
      <svg viewBox="0 0 16 16" fill="none" stroke="#fff" stroke-width="1.4"><circle cx="8" cy="8" r="6.5"/><ellipse cx="8" cy="8" rx="3" ry="6.5"/><path d="M1.5 8h13M3 4.5h10M3 11.5h10"/></svg>
      : www.samcorwell.com
    </li>
  </ul>
</section>

<!-- Page 2: about -->
<section class="page page--about">
  <svg class="page-art" viewBox="0 0 460 575" aria-hidden="true">
    <path d="M0 0H460V330C340 378 160 372 0 345Z" fill="url(#indigoFill)"/>
  </svg>
  <h2 class="section-title about-title">About Sam Corwell</h2>
  <div class="bio">
    <p>Whether it’s laugh out loud humour, inspiration or thought provoking anecdotes and perspective, Sam Corwell’s deeply moving presentations has it all.</p>
    <p>“An extraordinary mental and physical effort – something very, very special” is how Sir Alan Drake described Sam Corwell and the late Tom Ellery’s incredible achievement in winning the inaugural Ocean Rowing Race.</p>
    <p>Marathon rowing champion Sam Corwell has been a New Zealand International rowing representative for 16 years. Sam’s numerous rowing achievements include World Champs silver, Commonwealth gold and a world record on the indoor rowing machine.</p>
    <p>Sam represented New Zealand at the Atlanta Olympics and published ‘The Open Rower’ on how he and Tom Ellery captured headlines around the world winning the grueling and inaugural Ocean Rowing Race in 41 days. He then led teams to successful defenses in the next two editions making it a 3-peat of victories for New Zealand.</p>
    <p>He is co-organiser of the ‘Riverside 100’ (www.riverside100.kiwi), ‘The Grand Race’ (www.thegrandrace.co.nz), an annual rowing 8s clash between Riverside and leading international universities on the home river. His also recently conceived and managed a rowing expedition across the Tasman Sea.</p>
    <p>Ambitious goal-setting, teamwork and overcoming adversity in multiple Ocean Rowing Race campaigns is the spine of Sam’s presentations, sandwiching the challenge of following his brother Kevin’s journey into Cambodia’s Khmer Rouge genocide www.brotherstory.co.nz (optional topic). Powerful inspiring messages on tenacity, hope, love and the last human freedom: the power to choose your attitude and how you respond in a given situation. The humour, the insights and the emotional turning points have audiences spellbound.</p>
    <p>Sam will inspire you to pursue your dreams whatever they may be, to take on new challenges, overcoming hardship against the odds and know that with passion anything is possible!</p>
    <p>It doesn’t hurt to be just a little bit crazy too!</p>
    <p>Sam’s life is about following the dream, decision making, commitment, team building, goal setting, planning, focus, determination, positive thinking and, of course, winning!</p>
  </div>
  <h2 class="clients-title">What clients are saying …..</h2>
  <div class="quote-row" style="top:408px">
    <div class="client-tag">Helen Ward, HR Manager, Dairyfield</div>
    <p class="client-quote">“Sam has a remarkable story, told in a clever and compelling way. He is able to engage deeply with his audience; he made us laugh, cry and most importantly think deeply, as leaders, about our role in the world. One of the best!”</p>
  </div>
  <div class="quote-row" style="top:447px">
    <div class="client-tag">Kate Morgan, Seawatch<br>Conference Attendee</div>
    <p class="client-quote">You are the second only speaker who made me cry and laugh and feel great all in one short time period, thank you so much for everything you do, and have done…..</p>
  </div>
  <div class="quote-row" style="top:481px">
    <div class="client-tag">Jon Barrett, CEO Southport<br>International Airport</div>
    <p class="client-quote">“Kids Care Trust was looking for an inspirational speaker who would reflect the passion, the hope and the commitment exhibited by KCT and its members. When I set out to look for such a person Sam Corwell’s name kept bubbling to the surface and I’m delighted I made the phone call. Sam your speech is probably the most inspiring talk I have ever listened to. Your story is an amazing one delivered in a passionate and yet entertaining manner.”</p>
  </div>
  <div class="quote-row" style="top:550px">
    <div class="client-tag">Mark Penrose, Penrose Realty</div>
    <p class="client-quote">“… hearing your story was more inspirational than all the traditional “motivational” type trainers put together.”</p>
  </div>
</section>

<!-- Page 3: praise and photos -->
<section class="page page--praise">
  <svg class="page-art" viewBox="0 0 460 575" aria-hidden="true">
    <defs>
      <linearGradient id="seaFill" x1="0" y1="0" x2="0" y2="1">
        <stop offset="0" stop-color="#6fa7d6"/><stop offset="1" stop-color="#1f4f8c"/>
      </linearGradient>
      <linearGradient id="portraitFill" x1="0" y1="0" x2="1" y2="1">
        <stop offset="0" stop-color="#4a4a4a"/><stop offset="1" stop-color="#a8876c"/>
      </linearGradient>
    </defs>
    <path d="M0 0H460V55C330 95 150 98 0 70Z" fill="url(#indigoFill)"/>
    <path d="M0 70C150 98 330 95 460 55V66C330 108 150 110 0 82Z" fill="url(#silverFill)"/>
    <rect x="0" y="268" width="460" height="134" fill="url(#indigoFill)"/>
    <rect x="0" y="272" width="170" height="126" fill="url(#seaFill)" role="img" aria-label="Photo of two rowers celebrating aboard their ocean rowing boat"/>
    <rect x="182" y="272" width="86" height="126" fill="url(#portraitFill)" role="img" aria-label="Portrait photo of the speaker gesturing while talking"/>
    <rect x="278" y="272" width="182" height="126" fill="url(#seaFill)" role="img" aria-label="Photo of the rowers arriving in harbour with boats around them"/>
    <path d="M0 553C150 540 310 538 460 536V575H0Z" fill="url(#indigoFill)"/>
    <path d="M0 547C150 534 310 532 460 530V536C310 538 150 540 0 553Z" fill="url(#silverFill)"/>
  </svg>
  <div class="quote-row" style="top:112px">
    <div class="client-tag">Grant Miller, Harbor Country Head</div>
    <p class="client-quote">Sam was unbelievable, amazing, so well received, such a lovely guy, so humble. Had some of the audience in tears.</p>
  </div>
  <div class="quote-row" style="top:150px">
    <div class="client-tag">Sarah Bell, Plainview<br>Regional Council</div>
    <p class="client-quote">It was both an honour and a pleasure to be your host. The whole audience was captivated by your speech from start to finish. The clever way it was put together and how you incorporated our theme was fantastic. Your speech was truly inspirational and I personally have taken a lot out of it. The perspective on how I view challenges will change going forward as I am sure many others will too. I read a quote the other day that said ‘Don’t wait for sleep to dream’ and I think that sums it up nicely.</p>
  </div>
  <div class="quote-row" style="top:230px">
    <div class="client-tag">Lewis Foster, Petrolane</div>
    <p class="client-quote">“One regular conference goer said I could organise another 50 conferences and not see a presentation as good as that.”</p>
  </div>
  <div class="quote-row" style="top:415px">
    <div class="client-tag">Hannah Lowe, Harbor EA to<br>Country Head</div>
    <p class="client-quote">We have received nothing but the highest praise for your open and honest talk – many people have been deeply moved by your story and it was the highlight of the sessions.</p>
  </div>
  <div class="quote-row" style="top:455px">
    <div class="client-tag">Julia Evans, Faculty Management,<br>Ridgeport</div>
    <p class="client-quote">“Listening to Sam speak is a breath of fresh air! Too often we come across heroes that seem untouchable, unattainable. But Sam’s earthy humour and humble nature coupled with an unwavering drive and determination gives his story palpable appeal and something that the everyday person can truly connect with. Communicating with a passion that is infectious, Sam’s story is one of triumph and tragedy and provides any listener the inspiration to get beyond the mindset of ‘just getting by’ when enduring tough or challenging times. He imparts the wisdom and notion that self- belief is critical and more importantly ‘possible’ for every one of us to achieve on our own personal journey to success.”</p>
  </div>
</section>

<!-- Page 4: closing -->
<section class="page page--closing">
  <svg class="page-art" viewBox="0 0 460 575" aria-hidden="true">
    <defs>
      <linearGradient id="circleFill" x1="0" y1="0" x2="1" y2="1">
        <stop offset="0" stop-color="#8a8f8a"/><stop offset=".5" stop-color="#c98a73"/><stop offset="1" stop-color="#4e5a4a"/>
      </linearGradient>
    </defs>
    <path d="M0 0H460V30C330 58 150 62 0 44Z" fill="url(#indigoFill)"/>
    <path d="M0 44C150 62 330 58 460 30V40C330 70 150 73 0 54Z" fill="url(#silverFill)"/>
    <path d="M0 332C130 318 300 300 460 296V306C300 310 130 328 0 342Z" fill="url(#silverFill)"/>
    <path d="M0 342C130 328 300 310 460 306V575H0Z" fill="url(#indigoFill)"/>
    <circle cx="113" cy="440" r="88" fill="#fff"/>
    <circle cx="113" cy="440" r="84" fill="url(#circleFill)" role="img" aria-label="Photo of the speaker being presented with flowers in front of a film camera"/>
  </svg>
  <div class="quote-row" style="top:86px">
    <div class="client-tag">Capt Robin Buckley,<br>Coastal Defense Force</div>
    <p class="client-quote client-quote--spaced">Sam was outstanding. As requested he arrived early and set himself up with minimal assistance using our equipment. He was seated at the top table with some of our senior ranked officers and clearly struck a rapport early on, he skillfully (craftily) knitted some of this into the early part of his talk which was captivating and all were taken along on the roller coaster journey he portrays. He managed to lift the room initially before plummeting down into a deep and (not depressing) emotional low. This is done in such a way that he brings you along with him before raising your spirits once more and filling the room with laughter at the talks close.<br>Sam cleverly molded his message around his audience and expressed great respect for the military people in the room. This was appreciated.<br>I would highly recommend Sam to any audience.</p>
  </div>
  <div class="quote-row" style="top:234px">
    <div class="client-tag">Graham Peters, PE Association</div>
    <p class="client-quote client-quote--spaced">“I thought that you would be outstanding concluding Conference but I could not have expected the performance that you delivered. It blew everyone away Sam and it got in touch with their humanity which is what I wanted Physical Educators to go back to and to discover the power within. Thanks so very much for providing a conclusion to Conference that was extraordinarily powerful with such an invaluable message for all present.”</p>
  </div>
  <p class="closing-quote">“The speaker was one of the most powerful<br>I have listened to in years……incredible!”<small>- Feedback taken from Conference</small></p>
  <p class="site-link">www.samcorwell.com</p>
</section>

</body>
</html>
```